Photojournalism/photography business needs a simple, timeless & professional letterhead design

We need a letterhead design for photography/photojournalism business called 'qolvb', no capitals.

The letterhead needs to be:
- simple
- professional
- timeless
- easy to read
- consists of at least 2 colors to make it stands out.

We do mainly editorial photography, photo articles for various publications, travel, businesses, as well as people such as family and kids.

The final design should communicate professionalism, easy identification, attention grabbing, even if it has to be found among a stack of various papers on the clients' desks.

Target Market(s)

Various publications.

Industry/Entity Type

Business

Requirements
Must have
• Please use the logo attached.

```html
<!DOCTYPE html>
<html lang="en">
<head>
<meta charset="utf-8">
<title>qolvb letterhead</title>
<link href="https://fonts.googleapis.com/css2?family=Titillium+Web:wght@400;700&display=swap" rel="stylesheet">
<style>
  :root {
    --brand-red: #ed1c24;
    --ink-dark: #3a3a3a;
    --ink-body: #4a4a4a;
    --divider: #b5b5b5;
    --paper: #ffffff;
  }
  html, body {
    margin: 0;
    padding: 0;
    overflow: hidden;
    background: var(--paper);
  }
  .letterhead {
    position: relative;
    width: 849px;
    height: 1200px;
    overflow: hidden;
    background: var(--paper);
    font-family: "Titillium Web", Arial, sans-serif;
  }
  .letterhead__art {
    position: absolute;
    inset: 0;
    width: 849px;
    height: 1200px;
  }
  .art-red { fill: var(--brand-red); }
  .art-paper { fill: var(--paper); }
  .brand {
    position: absolute;
    left: 48px;
    top: 50px;
    display: flex;
    align-items: center;
    gap: 12px;
  }
  .brand__mark {
    width: 22px;
    height: 22px;
    background: var(--brand-red);
  }
  .brand__name {
    margin: 0;
    font-size: 72px;
    font-weight: 700;
    line-height: 1;
    letter-spacing: -1px;
    color: var(--ink-dark);
  }
  .contact-bar {
    position: absolute;
    left: 157px;
    right: 0;
    top: 1148px;
    height: 26px;
    display: flex;
    align-items: center;
  }
  .contact-bar__rule {
    height: 3px;
    background: var(--brand-red);
  }
  .contact-bar__rule--lead { width: 60px; margin-right: 10px; }
  .contact-bar__rule--tail { flex: 1; margin-left: 8px; }
  .contact-item {
    font-size: 15px;
    letter-spacing: 0.6px;
    color: var(--ink-body);
    white-space: nowrap;
  }
  .contact-item__label,
  .contact-item__accent {
    font-weight: 700;
    color: var(--brand-red);
  }
  .contact-bar__sep {
    width: 1px;
    height: 26px;
    background: var(--divider);
    margin: 0 11px;
  }
</style>
</head>
<body>
<div class="letterhead">
  <svg class="letterhead__art" viewBox="0 0 637 900" preserveAspectRatio="none" aria-hidden="true">
    <defs>
      <radialGradient id="corner-shadow" cx="0.5" cy="0.5" r="0.5">
        <stop offset="0" stop-color="#000" stop-opacity="0.14"/>
        <stop offset="1" stop-color="#000" stop-opacity="0"/>
      </radialGradient>
    </defs>
    <!-- top-right band -->
    <polygon class="art-red" points="448,0 637,0 637,540"/>
    <polygon class="art-paper" points="568,82 626,82 637,112 637,282"/>
    <!-- soft edge shadow -->
    <ellipse cx="640" cy="678" rx="90" ry="26" fill="url(#corner-shadow)"/>
    <!-- bottom-left band -->
    <path class="art-red" d="M0,460 L98,765 Q120,835 118,900 L0,900 Z"/>
    <path class="art-paper" d="M0,612 L58,795 Q70,845 66,900 L30,900 Q33,852 20,812 L0,752 Z"/>
  </svg>

  <header class="brand">
    <h1 class="brand__name">qolvb</h1>
    <span class="brand__mark"></span>
  </header>

  <footer class="contact-bar">
    <span class="contact-bar__rule contact-bar__rule--lead"></span>
    <span class="contact-item"><span class="contact-item__label">Tel:</span> 000 000</span>
    <span class="contact-bar__sep"></span>
    <span class="contact-item"><span class="contact-item__label">Fax:</span> 000 000</span>
    <span class="contact-bar__sep"></span>
    <span class="contact-item"><span class="contact-item__label">Email:</span> info@qolvb.com</span>
    <span class="contact-bar__sep"></span>
    <span class="contact-item">www.<span class="contact-item__accent">qolvb</span>.com</span>
    <span class="contact-bar__rule contact-bar__rule--tail"></span>
  </footer>
</div>
</body>
</html>
```